Business Card Design Project

Want a modern business card.
Concern is that our email address is long and thus poses a design challenge.
Items like the company name can be omitted from text as it will be available via the logo.

Example:
Gerald Tunstall
President / CEO
Cell 555.304.1182
Office 555.617.2093
geraldt@korvantsolutionsgroup.example
www.korvantsolutionsgroup.example

Target Market(s)

Technical and executive level members of Information Technology companies in the Healthcare industry.

Industry/Entity Type

Business

Colors

Designer to choose colors to be used in the design.

Requirements
Nice to have
• Raised logo, but I am open.

```html
<!DOCTYPE html>
<html lang="en">
<head>
<meta charset="utf-8">
<title>Korvant Solutions Group – Business Card</title>
<link rel="stylesheet" href="https://fonts.googleapis.com/css2?family=Cinzel:wght@700&family=Questrial&family=Arimo:wght@400&display=swap">
<style>
  :root {
    --backdrop: #c9f5dc;
    --card-white: #ffffff;
    --brand-blue: #0a2f9a;
    --brand-blue-deep: #0a2173;
    --brand-blue-bright: #0538c8;
    --brand-red: #e3140f;
    --text-light: #ffffff;
  }
  * { box-sizing: border-box; margin: 0; padding: 0; }
  html, body {
    width: 1200px;
    height: 856px;
    overflow: hidden;
    background: var(--backdrop);
  }
  .stage {
    position: relative;
    width: 1200px;
    height: 856px;
  }
  .card {
    position: absolute;
    width: 560px;
    height: 320px;
    border-radius: 34px;
    overflow: hidden;
    box-shadow: 0 10px 26px rgba(0, 60, 40, 0.18);
  }

  /* Front */
  .card-front {
    left: 90px;
    top: 450px;
    background: var(--card-white);
  }
  .card-front .red-band {
    position: absolute;
    inset: 0;
    width: 100%;
    height: 100%;
  }
  .card-front .brand-name {
    position: absolute;
    left: 0;
    right: 0;
    top: 92px;
    text-align: center;
    font-family: "Cinzel", serif;
    font-weight: 700;
    font-size: 25px;
    letter-spacing: 0.5px;
    color: var(--brand-blue);
  }
  .card-front .person {
    position: absolute;
    left: 0;
    right: 0;
    top: 212px;
    text-align: center;
    color: var(--text-light);
  }
  .card-front .person-name {
    font-family: "Cinzel", serif;
    font-weight: 700;
    font-size: 15px;
    letter-spacing: 0.6px;
  }
  .card-front .person-title {
    margin-top: 3px;
    font-family: "Arimo", sans-serif;
    font-size: 12.5px;
  }

  /* Back */
  .card-back {
    left: 560px;
    top: 90px;
    background: linear-gradient(160deg, var(--brand-blue-deep) 0%, var(--brand-blue) 55%, var(--brand-blue-bright) 100%);
  }
  .card-back .contact {
    position: absolute;
    right: 30px;
    bottom: 34px;
    text-align: right;
    font-family: "Questrial", sans-serif;
    font-size: 12.5px;
    line-height: 1.7;
    color: var(--text-light);
  }
  .card-back .contact-label { opacity: 0.85; }
  .card-back .contact-line { display: flex; justify-content: flex-end; align-items: center; gap: 6px; }
  .card-back .icon {
    display: inline-block;
    width: 10px;
    height: 9px;
    border: 1.5px solid var(--text-light);
    border-radius: 2px;
    margin-left: 8px;
  }
  .card-back .icon:first-child { margin-left: 0; }
</style>
</head>
<body>
  <main class="stage">
    <section class="card card-back" aria-label="Business card back">
      <div class="contact">
        <div class="contact-line">
          <span><span class="contact-label">Cell</span> 555.304.1182 <span class="contact-label">Office</span> 555.617.2093</span>
        </div>
        <div class="contact-line">
          <span class="icon"></span><span>geraldt@korvantsolutionsgroup.example</span>
          <span class="icon"></span><span>www.korvantsolutionsgroup.example</span>
        </div>
      </div>
    </section>

    <section class="card card-front" aria-label="Business card front">
      <svg class="red-band" viewBox="0 0 560 320" preserveAspectRatio="none" aria-hidden="true">
        <path d="M0 205 C 180 175, 380 145, 560 128 L560 320 L0 320 Z" fill="var(--brand-red)"/>
      </svg>
      <div class="brand-name">Korvant Solutions Group</div>
      <div class="person">
        <div class="person-name">GERALD TUNSTALL</div>
        <div class="person-title">President / CEO</div>
      </div>
    </section>
  </main>
</body>
</html>
```